Business Card Tech Company
Veradon Corp
Project: Business Card Tech Company
Business Card Tech Company -
Creative Brief
Simple
Marcel Dufresne
CEO
2745 Rue Belcourt, Québec, QC G2K 3P7, Canada
mdufresne@veradoncorp-example.com
www.veradoncorp-example.com
You can add Twitter @veradoncorp We are very open to different designs, We will provide fast feedback, You can try many styles and many fonts, Right now, our slogan is: the world made yours. You can put it on some designs if it fits well, consider we might want to change it.
We would like a back mostly visual, without much info.

```html
<!DOCTYPE html>
<html lang="en">
<head>
<meta charset="utf-8">
<title>Veradon Corp — Business Card</title>
<link rel="stylesheet" href="https://fonts.googleapis.com/css2?family=Ubuntu:wght@400;500&display=swap">
<style>
  :root {
    --stage: #e4e6e9;
    --card: #ffffff;
    --card-shade: #eef1f4;
    --brand-blue: #1e7fd0;
    --brand-blue-light: #45a6ec;
    --ink: #4a4f55;
    --ink-soft: #7b8188;
    --rule: #9fcbef;
    --deco-grey: #d7dbe0;
  }
  * { box-sizing: border-box; margin: 0; padding: 0; }
  html, body { width: 1200px; height: 797px; overflow: hidden; }
  body {
    background: var(--stage);
    font-family: "Ubuntu", sans-serif;
    display: flex;
    align-items: center;
    justify-content: center;
    gap: 60px;
  }
  .card {
    width: 520px;
    height: 297px;
    border-radius: 14px;
    background: linear-gradient(160deg, var(--card) 55%, var(--card-shade));
    box-shadow: 0 6px 22px rgba(0,0,0,0.14);
    position: relative;
    overflow: hidden;
  }
  /* Front: contact side */
  .card-front .deco-circle {
    position: absolute;
    left: -120px;
    top: 20px;
    width: 260px;
    height: 260px;
    border-radius: 50%;
    background: var(--deco-grey);
    opacity: 0.55;
  }
  .contact {
    position: absolute;
    right: 34px;
    top: 62px;
    text-align: right;
    width: 330px;
  }
  .contact .name {
    color: var(--brand-blue);
    font-size: 19px;
    font-weight: 500;
  }
  .contact .title {
    color: var(--ink-soft);
    font-size: 12px;
    margin-top: 3px;
  }
  .contact .rule {
    height: 1px;
    background: linear-gradient(90deg, transparent, var(--rule));
    margin: 14px 0 16px;
  }
  .contact ul { list-style: none; }
  .contact li {
    display: flex;
    justify-content: flex-end;
    align-items: flex-start;
    gap: 10px;
    color: var(--ink);
    font-size: 12px;
    line-height: 1.45;
    margin-bottom: 9px;
  }
  .contact li svg { flex: none; margin-top: 2px; }
  /* Back: brand side */
  .card-back {
    background: linear-gradient(180deg, var(--card) 40%, #e7eef5);
  }
  .brand {
    position: absolute;
    left: 0; right: 0; top: 110px;
    display: flex;
    align-items: center;
    justify-content: center;
    gap: 14px;
  }
  .brand .mark {
    width: 44px; height: 44px;
    border-radius: 50%;
    background: var(--brand-blue);
  }
  .brand .wordmark {
    color: var(--brand-blue);
    font-size: 40px;
    font-weight: 500;
  }
  .website {
    position: absolute;
    left: 0; right: 0; top: 176px;
    text-align: center;
    color: var(--brand-blue);
    font-size: 13px;
  }
</style>
</head>
<body>
  <section class="card card-front" aria-label="Business card front">
    <div class="deco-circle"></div>
    <div class="contact">
      <p class="name">Marcel Dufresne</p>
      <p class="title">CEO</p>
      <div class="rule"></div>
      <ul>
        <li>
          <span>2745 Rue Belcourt, Québec, QC<br>G2K 3P7, Canada</span>
          <svg width="12" height="12" viewBox="0 0 12 12" aria-hidden="true"><path d="M1 6 L6 1.5 L11 6 V11 H7.5 V8 H4.5 V11 H1 Z" fill="var(--brand-blue)"/></svg>
        </li>
        <li>
          <span>418-555-0142</span>
          <svg width="12" height="12" viewBox="0 0 12 12" aria-hidden="true"><rect x="3" y="0.5" width="6" height="11" rx="1.2" fill="var(--brand-blue)"/><rect x="4" y="2" width="4" height="6.5" fill="#fff"/></svg>
        </li>
        <li>
          <span>mdufresne@veradoncorp-example.com</span>
          <svg width="12" height="12" viewBox="0 0 12 12" aria-hidden="true"><rect x="0.5" y="2.5" width="11" height="7.5" rx="1" fill="var(--brand-blue)"/><path d="M1 3 L6 7 L11 3" stroke="#fff" stroke-width="1" fill="none"/></svg>
        </li>
      </ul>
    </div>
  </section>

  <section class="card card-back" aria-label="Business card back">
    <div class="brand">
      <span class="mark"></span>
      <span class="wordmark">Veradon</span>
    </div>
    <p class="website">www.veradoncorp-example.com</p>
  </section>
</body>
</html>
```